E learning Platform for privacy

Current website is as below and its more of a shell.
I need someone to take the text and content and design it properly.
https://study.norvalhub.example/

After that, design has to be implemented with quillbrick and wordpress
https://quillbrick.example/

```html
<!DOCTYPE html>
<html lang="en">
<head>
<meta charset="utf-8">
<title>NORVAL Learning Centre</title>
<link rel="stylesheet" href="https://fonts.googleapis.com/css2?family=Anton&family=Montserrat:wght@300;400;500;600;700&display=swap">
<style>
:root{
  --orange:#f08a24;
  --orange-deep:#e85f2a;
  --orange-grad:linear-gradient(90deg,#f39a2a 0%,#ee7a26 60%,#e8602a 100%);
  --ink:#1f1f1f;
  --grey:#777;
  --hero-dark:#4b3c31;
  --footer:#111214;
  --white:#fff;
}
*{margin:0;padding:0;box-sizing:border-box}
html,body{width:1200px;height:4198px;overflow:hidden}
body{position:relative;font-family:'Montserrat',sans-serif;color:var(--ink);background:var(--white)}
.abs{position:absolute}
.center{text-align:center}
.accent{color:var(--orange)}
.btn{position:absolute;display:flex;align-items:center;justify-content:center;border-radius:30px;background:var(--orange-deep);color:var(--white);font-size:17px;font-weight:500;letter-spacing:.5px}

/* header */
.site-header{left:0;top:0;width:1200px;height:82px;background:var(--orange-grad)}
.logo-plate{left:0;top:0;width:322px;height:82px;background:var(--white);border-radius:0 41px 41px 0}
.brand{position:absolute;text-align:center}
.brand-name{font-weight:700;color:var(--orange-deep);letter-spacing:4px;line-height:1}
.brand-tag{font-size:9px;letter-spacing:5px;color:var(--ink);margin-top:4px}
.nav{left:478px;top:34px;font-size:14px;color:var(--white);font-weight:500}
.nav span{position:absolute;white-space:nowrap}
.register{left:1009px;top:22px;width:112px;height:40px;font-size:14px}

/* hero */
.hero{left:0;top:82px;width:1200px;height:575px;background:linear-gradient(100deg,#3f3a36 0%,#6b5e52 40%,#9c8a78 60%,#4b3c31 100%)}
.hero-tab{left:480px;top:656px}
.hero-title{left:78px;top:248px;font-family:'Anton',sans-serif;font-size:54px;line-height:54px;color:var(--white);letter-spacing:1px}
.hero-sub{left:82px;top:368px;font-size:16px;line-height:24px;color:var(--white)}
.hero-cta{left:82px;top:429px;width:176px;height:49px}
.dots{left:1154px;top:323px}
.dots i{display:block;width:14px;height:14px;border-radius:50%;background:var(--white);margin-bottom:13px}
.dots i.on{background:var(--orange)}

/* welcome */
.h2{font-size:42px;font-weight:400;line-height:52px}
.lead{font-size:14px;line-height:27px;color:var(--grey)}
.stat-ring{width:84px;height:84px;border-radius:50%;background:#fdeee0;display:flex;align-items:center;justify-content:center}
.stat-num{font-size:30px;font-weight:700}
.stat-label{font-size:15px;color:#555}

/* featured */
.featured{left:78px;top:1276px;width:1122px;height:520px;background:var(--orange-grad);border-radius:260px 0 0 260px}
.featured-title{left:163px;top:1462px;font-size:40px;font-weight:600;line-height:42px;color:var(--white)}
.view-more{left:161px;top:1568px;width:167px;height:49px}
.course-card{position:absolute;top:1338px;width:313px;height:396px;background:var(--white);overflow:hidden}
.course-img{width:313px;height:209px}
.ribbon{position:absolute;left:-34px;top:26px;width:140px;height:30px;background:var(--orange-deep);transform:rotate(-45deg);color:var(--white);font-weight:700;font-size:16px;text-align:center;line-height:30px}
.course-body{padding:26px 20px 0}
.course-title{font-size:20px;font-weight:600;line-height:25px}
.meta{display:flex;align-items:center;gap:10px;font-size:14px;color:#555;margin-top:16px}

/* why */
.feature{position:absolute;width:300px;text-align:center}
.feature .ring{width:84px;height:84px;border-radius:50%;background:#fdeee0;margin:0 auto;display:flex;align-items:center;justify-content:center}
.feature .ring.solid{background:var(--orange-deep)}
.feature h3{font-size:20px;font-weight:600;line-height:25px;margin-top:30px}
.feature p{font-size:14px;line-height:25px;color:var(--grey);margin:12px auto 0;width:230px}

/* testimonial */
.quote-band{left:0;top:2678px;width:760px;height:416px;background:var(--orange-grad);border-radius:0 208px 208px 0}
.quote-title{left:78px;top:2762px;font-size:40px;font-weight:600;color:var(--white)}
.quote-text{left:78px;top:2838px;width:440px;font-size:16px;line-height:29px;color:var(--white)}
.client{left:78px;top:2974px;font-size:21px;color:var(--white)}
.avatar{position:absolute;border-radius:50%;border:4px solid var(--white)}

/* blog */
.blog-card{position:absolute;top:3236px;width:312px;height:466px;background:var(--white);box-shadow:0 4px 16px rgba(0,0,0,.12)}
.blog-img{width:312px;height:207px}
.blog-body{padding:22px 18px 0}
.blog-title{font-size:26px;font-weight:400}
.blog-date{font-size:14px;color:var(--orange);margin-top:8px}
.blog-text{font-size:14px;line-height:27px;color:var(--grey);margin-top:14px}
.read-more{position:absolute;right:18px;bottom:20px;font-size:13px;font-weight:600;color:var(--orange-deep);text-decoration:underline}

/* newsletter */
.newsletter{left:0;top:3760px;width:1200px;height:103px;background:var(--orange-grad)}
.newsletter-title{left:156px;top:3792px;font-size:33px;color:var(--white);font-weight:400}
.email-field{left:566px;top:3787px;width:466px;height:52px;border-radius:26px;background:var(--white);font-size:14px;color:#555;padding:17px 22px}
.send{position:absolute;right:6px;top:6px;width:40px;height:40px;border-radius:50%;background:var(--orange-deep);display:flex;align-items:center;justify-content:center}

/* footer */
.footer{left:0;top:3863px;width:1200px;height:335px;background:var(--footer)}
.foot-title{font-size:20px;color:var(--orange)}
.sitemap li{list-style:none;font-size:14px;color:#ddd;height:31px;display:flex;align-items:center}
.sitemap li::before{content:"";width:6px;height:6px;border-radius:50%;background:var(--orange);margin-right:12px}
.contact-line{position:absolute;right:80px;font-size:14px;color:#ddd;text-align:right;line-height:26px;display:flex;align-items:center;gap:18px}
.social{position:absolute;top:4032px;width:40px;height:40px;border-radius:50%;border:2px solid var(--orange)}
.rule{left:78px;top:4135px;width:1044px;height:1px;background:#333}
.copyright{left:0;top:4158px;width:1200px;font-size:14px;color:#bbb}
.copyright b{color:var(--orange);font-weight:600}
</style>
</head>
<body>

<!-- header -->
<header class="abs site-header"></header>
<div class="abs logo-plate"></div>
<div class="brand" style="left:70px;top:14px;width:190px">
  <div class="brand-name" style="font-size:38px">NORVAL</div>
  <div class="brand-tag">LEARNING CENTRE</div>
</div>
<nav class="abs nav">
  <span style="left:0">HOME</span>
  <span style="left:71px">BLOGS</span>
  <span style="left:150px">COURSES</span>
  <span style="left:244px">ABOUT US</span>
  <span style="left:342px">CONTACT US</span>
  <span style="left:462px">LOGIN</span>
</nav>
<div class="btn register">REGISTER</div>

<!-- hero -->
<section class="abs hero" role="img" aria-label="Smiling man with headphones studying at a laptop in a cafe"></section>
<svg class="abs hero-tab" width="240" height="44" viewBox="0 0 240 44">
  <path d="M0 0 C60 0 80 42 120 42 C160 42 180 0 240 0Z" fill="#5a4c40"/>
  <path d="M112 10 H128 M114 14 H126 M116 18 H124" stroke="#fff" stroke-width="1.5" stroke-dasharray="2 2"/>
</svg>
<h1 class="abs hero-title">Norval Privacy<br>Academy</h1>
<p class="abs hero-sub">Largest online e-learning resource for<br>data protection &amp; privacy</p>
<div class="btn hero-cta">GET TRAINED</div>
<div class="abs dots"><i></i><i></i><i></i><i class="on"></i><i></i></div>

<!-- welcome -->
<h2 class="abs h2 center" style="left:0;top:758px;width:1200px">Welcome To<br><span class="accent">(NORVAL)</span> Learning Centre</h2>
<p class="abs lead center" style="left:272px;top:890px;width:656px">Lorem Ipsum is simply dummy text of the printing and typesetting industry. Lorem Ipsum has been the industry's standard dummy text ever since the 1500s, when an unknown printer took a galley of type and scrambled it to make a type specimen book. It has survived not only five</p>

<div class="abs center" style="left:368px;top:1037px;width:150px">
  <div class="stat-ring" style="margin:0 auto"><svg width="40" height="40" viewBox="0 0 40 40" fill="none" stroke="#f08a24" stroke-width="1.6"><path d="M6 12 L20 6 L34 12 L20 18Z"/><path d="M13 15 V20 C13 25 27 25 27 20 V15"/><path d="M8 36 C9 28 31 28 32 36"/></svg></div>
  <div class="stat-num" style="margin-top:22px">6,375</div>
  <div class="stat-label">Enrolled Student</div>
</div>
<div class="abs center" style="left:525px;top:1037px;width:150px">
  <div class="stat-ring" style="margin:0 auto"><svg width="40" height="40" viewBox="0 0 40 40" fill="none" stroke="#f08a24" stroke-width="1.6"><rect x="5" y="7" width="30" height="20" rx="1"/><path d="M14 33 H26 M20 27 V33 M10 13 H24 M10 18 H30 M10 22 H20"/></svg></div>
  <div class="stat-num" style="margin-top:22px">144</div>
  <div class="stat-label">Lessons</div>
</div>
<div class="abs center" style="left:670px;top:1037px;width:150px">
  <div class="stat-ring" style="margin:0 auto"><svg width="40" height="40" viewBox="0 0 40 40" fill="none" stroke="#f08a24" stroke-width="1.6"><path d="M5 10 H16 L19 13 H35 V32 H5Z"/><path d="M17 18 L25 22.5 L17 27Z"/></svg></div>
  <div class="stat-num" style="margin-top:22px">169</div>
  <div class="stat-label">Videos</div>
</div>

<!-- featured courses -->
<section class="abs featured"></section>
<h2 class="abs featured-title">Featured<br>Courses</h2>
<div class="btn view-more">VIEW MORE</div>

<article class="course-card" style="left:448px">
  <div class="course-img" role="img" aria-label="Hands working with a laptop and paper charts on a desk" style="background:linear-gradient(135deg,#cfd6dc,#8e99a3)"></div>
  <div class="ribbon">FREE</div>
  <div class="course-body">
    <div class="course-title">How to Scale Social<br>Impact</div>
    <div class="meta"><svg width="14" height="14" viewBox="0 0 14 14" fill="none" stroke="#e85f2a" stroke-width="1.4"><rect x="1" y="2.5" width="12" height="10.5"/><path d="M1 6 H13 M4 1 V4 M10 1 V4"/></svg>Dec 19,2019</div>
    <div class="meta"><svg width="14" height="14" viewBox="0 0 14 14" fill="#e85f2a"><circle cx="7" cy="4" r="3.2"/><path d="M1 14 C1 8 13 8 13 14Z"/></svg>Mr.Example</div>
  </div>
</article>
<article class="course-card" style="left:782px">
  <div class="course-img" role="img" aria-label="Man with headset taking notes beside a laptop" style="background:linear-gradient(135deg,#d9d3cc,#8f8377)"></div>
  <div class="ribbon">FREE</div>
  <div class="course-body">
    <div class="course-title">Global Social<br>Enrepreneurship</div>
    <div class="meta"><svg width="14" height="14" viewBox="0 0 14 14" fill="none" stroke="#e85f2a" stroke-width="1.4"><rect x="1" y="2.5" width="12" height="10.5"/><path d="M1 6 H13 M4 1 V4 M10 1 V4"/></svg>Dec 18,2019</div>
    <div class="meta"><svg width="14" height="14" viewBox="0 0 14 14" fill="#e85f2a"><circle cx="7" cy="4" r="3.2"/><path d="M1 14 C1 8 13 8 13 14Z"/></svg>Mr.Example</div>
  </div>
</article>

<!-- why -->
<h2 class="abs h2 center" style="left:0;top:1853px;width:1200px">Why The <span class="accent">(NORVAL)</span> Learning<br>Centre?</h2>
<p class="abs lead center" style="left:262px;top:1968px;width:676px">Our mission at the Norval Privacy Academy (NORVAL) Learning Centre is to provide business and job opportunities, as well as to enhance personal and career advancement for data protection / privacy professionals.</p>

<div class="feature" style="left:142px;top:2084px">
  <div class="ring solid"><svg width="40" height="40" viewBox="0 0 40 40" fill="none" stroke="#fff" stroke-width="1.6"><circle cx="10" cy="24" r="3"/><circle cx="29" cy="9" r="3"/><rect x="24" y="20" width="10" height="8"/><path d="M10 27 V33 M13 24 H20 V9 H26 M20 24 H24"/></svg></div>
  <h3>Comprehensive<br>Roadmap</h3>
  <p>Our objective is to provide a comprehnsive competency roadmap, instead.</p>
</div>
<div class="feature" style="left:450px;top:2084px">
  <div class="ring"><svg width="40" height="40" viewBox="0 0 40 40" fill="none" stroke="#f08a24" stroke-width="1.6"><circle cx="13" cy="14" r="4"/><circle cx="26" cy="11" r="4"/><path d="M5 28 C6 20 20 20 21 26 M19 22 C22 16 33 17 34 23 M6 32 L18 30 L34 24"/></svg></div>
  <h3>Operational<br>Perspective</h3>
  <p>We cover a broad range of data protection topics from both a legal and.</p>
</div>
<div class="feature" style="left:760px;top:2084px">
  <div class="ring"><svg width="40" height="40" viewBox="0 0 40 40" fill="none" stroke="#f08a24" stroke-width="1.6"><rect x="9" y="5" width="22" height="30"/><path d="M14 11 H26 M14 15 H26 M14 19 H22"/><circle cx="20" cy="26" r="3"/></svg></div>
  <h3>Academic &amp; Internatio<br>-nal Certification</h3>
  <p>We partner with prominent universities in the region as well as international.</p>
</div>
<div class="feature" style="left:142px;top:2369px">
  <div class="ring"><svg width="40" height="40" viewBox="0 0 40 40" fill="none" stroke="#f08a24" stroke-width="1.6"><circle cx="20" cy="12" r="6"/><circle cx="20" cy="12" r="2"/><circle cx="10" cy="26" r="3"/><circle cx="30" cy="26" r="3"/><path d="M5 36 C5 30 15 30 15 36 M25 36 C25 30 35 30 35 36"/></svg></div>
  <h3>Modular Approach<br>&amp; Flexibility</h3>
  <p>All our courses are modular in nature to cater to the busy professional, meaning.</p>
</div>
<div class="feature" style="left:450px;top:2369px">
  <div class="ring"><svg width="40" height="40" viewBox="0 0 40 40" fill="none" stroke="#f08a24" stroke-width="1.6"><circle cx="20" cy="7" r="3"/><circle cx="10" cy="20" r="3"/><circle cx="30" cy="20" r="3"/><circle cx="20" cy="22" r="3"/><path d="M15 15 H25 M4 34 C4 27 16 27 16 34 M24 34 C24 27 36 27 36 34 M14 34 C14 29 26 29 26 34"/></svg></div>
  <h3>Network With<br>Other Peers</h3>
  <p>Participate in our online communities and discussion rooms and your .</p>
</div>
<div class="feature" style="left:760px;top:2369px">
  <div class="ring"><svg width="40" height="40" viewBox="0 0 40 40" fill="none" stroke="#f08a24" stroke-width="1.6"><rect x="12" y="12" width="16" height="16"/><path d="M20 4 V12 M20 28 V36 M4 20 H12 M28 20 H36"/><circle cx="20" cy="20" r="3"/></svg></div>
  <h3>Business and Job<br>Opportunities</h3>
  <p>Collaborate with other professionals on potential business opportunities.</p>
</div>

<!-- testimonial -->
<section class="abs quote-band"></section>
<h2 class="abs quote-title">What People Say</h2>
<p class="abs quote-text">" Lorem Ipsum is simply dummy text of the printing and typesetting industry. Lorem Ipsum has been the industry's standard dummy text ever since the 1500s, when an unknown printer took a "</p>
<div class="abs client">&#8212;&nbsp; Client Name</div>
<div class="avatar" role="img" aria-label="Portrait of a smiling young woman among colleagues" style="left:644px;top:2790px;width:196px;height:196px;background:linear-gradient(135deg,#6b4b38,#c9a48a)"></div>
<svg class="abs" style="left:824px;top:2788px" width="60" height="50" viewBox="0 0 60 50" fill="#f08a24"><path d="M2 48 C2 22 10 8 26 2 L28 8 C18 14 16 22 16 28 H26 V48Z"/><path d="M32 48 C32 22 40 8 56 2 L58 8 C48 14 46 22 46 28 H56 V48Z"/></svg>
<div class="avatar" role="img" aria-label="Portrait of a woman with wavy hair" style="left:997px;top:2707px;width:106px;height:106px;background:linear-gradient(135deg,#8a5a3d,#d8b49a)"></div>
<div class="avatar" role="img" aria-label="Portrait of a smiling blonde woman" style="left:959px;top:2933px;width:106px;height:106px;background:linear-gradient(135deg,#c7b09a,#efe2d6)"></div>

<!-- blog -->
<h2 class="abs h2 center" style="left:0;top:3150px;width:1200px">Latest <span class="accent">Blog</span></h2>
<article class="blog-card" style="left:277px">
  <div class="blog-img" role="img" aria-label="Hands working with a laptop and paper charts on a desk" style="background:linear-gradient(135deg,#cfd6dc,#8e99a3)"></div>
  <div class="blog-body">
    <div class="blog-title">How To Write Blog</div>
    <div class="blog-date">December 18, 2019</div>
    <p class="blog-text">Writing a blog post is a little like driving; you can study the highway code (or read articles telling you how to write a blog post) for months,</p>
  </div>
  <span class="read-more">Read More &#9656;</span>
</article>
<article class="blog-card" style="left:611px">
  <div class="blog-img" role="img" aria-label="Two colleagues looking at a laptop together in an office" style="background:linear-gradient(135deg,#9aa6b0,#4f5b66)"></div>
  <div class="blog-body">
    <div class="blog-title">Hello world!</div>
    <div class="blog-date">December 13, 2019</div>
    <p class="blog-text">Writing a blog post is a little like driving; you can study the highway code (or read articles telling you how to write a blog post) for months,</p>
  </div>
  <span class="read-more">Read More &#9656;</span>
</article>

<!-- newsletter -->
<section class="abs newsletter"></section>
<h2 class="abs newsletter-title">SignUp For Newsletter !</h2>
<div class="abs email-field">Enter Email *
  <span class="send"><svg width="18" height="18" viewBox="0 0 18 18" fill="none" stroke="#fff" stroke-width="1.6"><path d="M2 9 L16 2 L11 16 L8 10Z M8 10 L16 2"/></svg></span>
</div>

<!-- footer -->
<footer class="abs footer"></footer>
<div class="abs foot-title" style="left:78px;top:3893px">Sitemap</div>
<ul class="abs sitemap" style="left:78px;top:3936px">
  <li>Home</li><li>Blogs</li><li>Courses</li><li>About Us</li><li>Contact Us</li>
</ul>
<div class="brand" style="left:440px;top:3918px;width:320px">
  <div class="brand-name" style="font-size:58px">NORVAL</div>
  <div class="brand-tag" style="color:#fff;font-size:12px;letter-spacing:9px;margin-top:10px">LEARNING CENTRE</div>
</div>
<span class="social" style="left:508px"></span>
<span class="social" style="left:555px"></span>
<span class="social" style="left:603px"></span>
<span class="social" style="left:650px"></span>

<div class="abs foot-title" style="right:80px;top:3893px">Contact Us</div>
<div class="contact-line" style="top:3938px">
  <div>Eastvale<br>418 Harbor Lane, Eastvale,<br>TX 75000, USA</div>
  <svg width="18" height="24" viewBox="0 0 18 24" fill="none" stroke="#f08a24" stroke-width="2" style="align-self:flex-start;margin-top:4px"><path d="M9 23 C9 23 1 13 1 8.5 A8 8 0 0 1 17 8.5 C17 13 9 23 9 23Z"/><circle cx="9" cy="8.5" r="3"/></svg>
</div>
<div class="contact-line" style="top:4033px">
  <div>+1 (800) 555 01 23</div>
  <svg width="18" height="18" viewBox="0 0 18 18" fill="#f08a24"><path d="M4 1 L7 5 L5 7.5 C6 10 8 12 10.5 13 L13 11 L17 14 L15 17 C8 17 1 10 1 3Z"/></svg>
</div>
<div class="contact-line" style="top:4070px">
  <div>support@study.norvalhub.example</div>
  <svg width="18" height="14" viewBox="0 0 18 14" fill="#f08a24"><rect x="0" y="0" width="18" height="14" rx="1"/><path d="M1 1 L9 8 L17 1" stroke="#111214" stroke-width="1.5" fill="none"/></svg>
</div>
<div class="abs rule"></div>
<p class="abs copyright center">&copy;<b>NORVAL LEARNING CENTER</b> - 2020 All rights reserved.</p>

</body>
</html>
```